Cause bitches need love too!

I am creating an ad campaign. It will be a series of featured dogs in our shelter and they will contain a picture of the dog wich should be big enough to see on a yard sign and will change every week. I am placing the signs so that they lead you to the shelter. This is why I am also including the copy that says "you're almost there".

I have 4 tag lines:

1. Find unconditional Love.
2. She'll Love you furever!
3. He'll always listen.
4. Meet your new BFF

You're almost there 318 W Harrowgate Ln
Open 10 - 7/Tues-Sat

The dimensions for the sign are 24" wide and 18" high

Every week we will have a different picture of a different dog (hopefully last week's dog gets adopted). Anyhow, I am printing out yard signs, meaning that instead of printing 160 different signs it would be ideal just to replace the photo. So far the copy that is permanent is: "You're almost there. 318 W. Harrowgate Ln."

I could silhouette the image of the dog as well and super impose it on the sign, that's also a consideration, but ideally if I could have 4 tag lines I could print 40 signs of each and just replace the photo manually each week from my printer that would save costs.
Updates

Not enough designs to chose from and I edited the brief and committed to pay no matter what to increase the amount of designs as per your suggestions.

Target Market(s)

Animal lovers

Industry/Entity Type

Campaign

Font styles to use
Sans Serif

Colors

Designer to choose colors to be used in the design.

Requirements
Must have
• The dimensions for the sign are 24" wide and 18" high
Nice to have
• I want the signs to be hip, they should have a positive feel to them. You can alter the photos if you like. I am even open to new copy if you think something else works better.

```html
<!DOCTYPE html>
<html lang="en">
<head>
<meta charset="utf-8">
<title>Shelter Yard Sign Series</title>
<link rel="stylesheet" href="https://fonts.googleapis.com/css2?family=Open+Sans:wght@300;800&display=swap">
<style>
  :root {
    --board: #8b8b8b;
    --sign-white: #ffffff;
    --ink: #161616;
    --headline-shadow: rgba(18, 18, 18, 0.9);
    --backdrop-left: #cfc9c8;
    --backdrop-right: #dedad9;
    --coat-tan: #b98a4f;
    --coat-gold: #a7763d;
    --coat-dark: #3a2c1e;
  }
  * { margin: 0; padding: 0; box-sizing: border-box; }
  html, body {
    width: 1200px;
    height: 960px;
    overflow: hidden;
    background: var(--board);
    font-family: "Open Sans", Arial, sans-serif;
  }
  .sign-series {
    position: relative;
    width: 1200px;
    height: 960px;
  }
  .yard-sign {
    position: absolute;
    width: 500px;
    height: 374px;
    overflow: hidden;
    background: var(--sign-white);
    box-shadow: 0 16px 20px -10px rgba(0, 0, 0, 0.5);
  }
  .yard-sign--listen  { left: 68px;  top: 88px; }
  .yard-sign--furever { left: 602px; top: 88px; }
  .yard-sign--bff     { left: 68px;  top: 504px; }
  .yard-sign--love    { left: 602px; top: 504px; }

  .dog-photo {
    position: absolute;
    inset: 0 0 86px 0;
    background: linear-gradient(90deg, var(--backdrop-left), var(--backdrop-right));
  }
  .dog-photo__subject {
    position: absolute;
    left: 0;
    top: 8px;
    bottom: 0;
    width: 214px;
    border-top-right-radius: 90px 120px;
    background: linear-gradient(180deg, var(--coat-tan) 0%, var(--coat-gold) 55%, var(--coat-dark) 100%);
  }

  .tagline {
    position: absolute;
    right: 13px;
    bottom: 88px;
    text-align: right;
    color: var(--sign-white);
    font-weight: 800;
    text-transform: uppercase;
    line-height: 0.82;
    text-shadow: -4px 3px 0 var(--headline-shadow);
  }
  .tagline__line { display: block; white-space: nowrap; }

  .info-band {
    position: absolute;
    left: 0;
    right: 0;
    bottom: 0;
    height: 86px;
    background: var(--sign-white);
    color: var(--ink);
    text-align: center;
    text-transform: uppercase;
    padding-top: 6px;
  }
  .info-band__address {
    display: block;
    font-weight: 800;
    font-size: 34px;
    line-height: 1.1;
  }
  .info-band__hours {
    display: block;
    font-weight: 300;
    font-size: 28px;
    line-height: 1.1;
  }
</style>
</head>
<body>
<main class="sign-series">

  <article class="yard-sign yard-sign--listen">
    <div class="dog-photo" role="img" aria-label="Featured shelter dog, tan and black hound mix, tilting its head, on a soft gray backdrop"><div class="dog-photo__subject"></div></div>
    <h2 class="tagline">
      <span class="tagline__line" style="font-size:80px">He'll</span>
      <span class="tagline__line" style="font-size:71px">Always</span>
      <span class="tagline__line" style="font-size:105px">Listen</span>
    </h2>
    <footer class="info-band">
      <span class="info-band__address">318 W Harrowgate Ln</span>
      <span class="info-band__hours">Open Tuesday-Sunday till 7pm</span>
    </footer>
  </article>

  <article class="yard-sign yard-sign--furever">
    <div class="dog-photo" role="img" aria-label="Featured shelter dog, tan and black hound mix, tilting its head, on a soft gray backdrop"><div class="dog-photo__subject"></div></div>
    <h2 class="tagline">
      <span class="tagline__line" style="font-size:68px">She'll</span>
      <span class="tagline__line" style="font-size:62px">Love you</span>
      <span class="tagline__line" style="font-size:79px">Furever!</span>
    </h2>
    <footer class="info-band">
      <span class="info-band__address">318 W Harrowgate Ln</span>
      <span class="info-band__hours">Open Tuesday-Sunday till 7pm</span>
    </footer>
  </article>

  <article class="yard-sign yard-sign--bff">
    <div class="dog-photo" role="img" aria-label="Featured shelter dog, tan and black hound mix, tilting its head, on a soft gray backdrop"><div class="dog-photo__subject"></div></div>
    <h2 class="tagline">
      <span class="tagline__line" style="font-size:67px">Meet</span>
      <span class="tagline__line" style="font-size:93px">Your</span>
      <span class="tagline__line" style="font-size:86px">New BFF</span>
    </h2>
    <footer class="info-band">
      <span class="info-band__address">318 W Harrowgate Ln</span>
      <span class="info-band__hours">Open Tuesday-Sunday till 7pm</span>
    </footer>
  </article>

  <article class="yard-sign yard-sign--love">
    <div class="dog-photo" role="img" aria-label="Featured shelter dog, tan and black hound mix, tilting its head, on a soft gray backdrop"><div class="dog-photo__subject"></div></div>
    <h2 class="tagline">
      <span class="tagline__line" style="font-size:69px">Find</span>
      <span class="tagline__line" style="font-size:34px">Unconditional</span>
      <span class="tagline__line" style="font-size:134px">Love</span>
    </h2>
    <footer class="info-band">
      <span class="info-band__address">318 W Harrowgate Ln</span>
      <span class="info-band__hours">Open Tuesday-Sunday till 7pm</span>
    </footer>
  </article>

</main>
</body>
</html>
```